QM Studios needs and Interior Design Business card

I can do anything from Commercial to Residential and Free lance. Beginning to end in design selection process.
Need something to catch the eye of potential customers and vendors. From furniture to Tile and Cabinet selections. I can do it all.

Industry/Entity Type

Design Agency

Contact Information for Business Card

QM Studios- Design Consultanting Residential, Commerical
Maybe a cool detail background. Wall paper print that can have some texture

Font styles to use
Serif

Colors
709dcb
34a6d7
b868aa
e667a6
f59296
85acd3
ffffff
000000
5c5c5c

Requirements
Must have
• Square or Rectangular with Rounded edges
• Name
• Address
• Phone
• Email
Nice to have
• Some colored edges More simples not too busy
• Pattern detail in background.
Should not have
• Not too much color

```html
<!DOCTYPE html>
<html lang="en">
<head>
<meta charset="utf-8">
<title>QM Studios – Business Card</title>
<link rel="stylesheet" href="https://fonts.googleapis.com/css2?family=Josefin+Sans:wght@300;400&display=swap">
<style>
  :root {
    --backdrop: #5c5c5c;
    --card-pink: #f59296;
    --card-white: #ffffff;
    --ink: #2e2e2e;
    --dot-tone: #f1f1f1;
  }
  html, body {
    margin: 0;
    padding: 0;
    overflow: hidden;
  }
  .canvas {
    position: relative;
    width: 1200px;
    height: 1023px;
    background: var(--backdrop);
    font-family: "Josefin Sans", "Futura", sans-serif;
    color: var(--ink);
    overflow: hidden;
  }
  .card {
    position: absolute;
    left: 330px;
    width: 540px;
    height: 310px;
    border-radius: 10px;
    box-shadow: 0 10px 30px rgba(0,0,0,0.35);
    overflow: hidden;
  }
  .card-front {
    top: 150px;
    background: var(--card-pink);
  }
  .card-back {
    top: 560px;
    background: var(--card-white);
  }
  .brand {
    position: absolute;
    left: 44px;
    top: 112px;
    display: flex;
    align-items: center;
    gap: 14px;
  }
  .brand-circle {
    width: 54px;
    height: 54px;
    border: 3px solid var(--ink);
    border-radius: 50%;
    box-sizing: border-box;
    flex: none;
  }
  .brand-name {
    font-size: 23px;
    font-weight: 400;
    letter-spacing: 3px;
    white-space: nowrap;
  }
  .contact {
    position: absolute;
    left: 320px;
    top: 62px;
    font-weight: 300;
  }
  .contact-name {
    font-size: 30px;
    margin: 0 0 14px;
    font-weight: 300;
    white-space: nowrap;
  }
  .contact-line {
    font-size: 14px;
    margin: 0 0 4px;
    letter-spacing: 0.3px;
    white-space: nowrap;
  }
  .contact-address {
    margin-top: 18px;
  }
  .contact-address .contact-line {
    font-size: 16px;
    margin-bottom: 6px;
  }
  .dot-field {
    position: absolute;
    inset: 30px;
    background: var(--dot-tone);
    border-radius: 4px;
  }
</style>
</head>
<body>
  <div class="canvas">
    <section class="card card-front">
      <div class="brand">
        <div class="brand-circle"></div>
        <span class="brand-name">QM Studios</span>
      </div>
      <div class="contact">
        <p class="contact-name">Jane Marlow</p>
        <p class="contact-line">02 48 61 27 93</p>
        <p class="contact-line">janemarlow@qmmail.com</p>
        <div class="contact-address">
          <p class="contact-line">18 Linden Row</p>
          <p class="contact-line">PO BOX- 7120</p>
          <p class="contact-line">Harbourview</p>
        </div>
      </div>
    </section>
    <section class="card card-back">
      <div class="dot-field" role="img" aria-label="Fine black dot grid pattern on white"></div>
    </section>
  </div>
</body>
</html>
```